International business needs a web page design

We need a web page design for a new service that our new "sub-company" of our existing company will offer. We are based in Denmark, and our new "sub-company" is called 'Velkari'. The service we offer is automated server configuration and In-Depth monitoring, and optional operations support. Our monitoring has a lot of graphs (like those seen here: https://velkari.example/ with either black or white background ) and the website needs to communicate a sense of Security/safety and that our customers can relax, because we have the full overview of their service and servers. The website should not be with black background.

We deliver low price, high quality and professional operations - which we can do, because we automate it and have people with 15+ years of experience doing so.

We have attached :

Target Market(s)

Chief Technological officers (CTO's) and Developers (small business, run by developers) - who needs professional IT operations.

Industry/Entity Type

Business

Coding

Coded - Design and coding required

Number of Pages Required

3 page

Requirements
Must have
• Frontpage :
• A lot of visualization(some with people too) rather than a lot of text
• A short, describing text on front page telling what people get
• 3 steps showing people how it works. (Could be presented in a video placed on top of a big front image or perhaps with all 3 steps/pictures shown at the same time or perhaps in a completely different way).
Nice to have
• A big front image(perhaps a person with a cellphone showing graphs and a "all okay" message) with a text and the 3-steps pictures/or video on top of it
• 3 boxes under the front image/top of the site showing what benefits people get from the service
Should not have
• Not a black/dark site

```html
<!DOCTYPE html>
<html lang="en">
<head>
<meta charset="utf-8">
<title>Velkari – Dashboard</title>
<link rel="stylesheet" href="https://fonts.googleapis.com/css2?family=Nunito+Sans:wght@400;600;700;800&display=swap">
<style>
  :root{
    --ink:#2b2b2b;
    --ink-soft:#555;
    --muted:#9a9a9a;
    --blue:#1ba6dc;
    --blue-light:#45b9e6;
    --blue-dark:#0f86b8;
    --ok:#33a81d;
    --panel:#ffffff;
    --panel-tint:#f7f7f7;
    --line:#e6e6e6;
    --stage-a:#ececec;
    --stage-b:#dcdcdc;
    --footer:#ffffff;
    --social:#bdbdbd;
    --social-hot:#e2351c;
  }
  *{box-sizing:border-box;margin:0;padding:0}
  html,body{width:1200px;height:610px;overflow:hidden}
  body{font-family:"Nunito Sans",Arial,sans-serif;color:var(--ink);background:var(--footer);position:relative}
  .stage{position:absolute;left:0;top:0;width:1200px;height:520px;
    background:radial-gradient(ellipse at 30% 20%,#f4f4f4 0%,var(--stage-a) 45%,var(--stage-b) 100%)}
  .site-header{position:absolute;left:160px;top:20px;width:880px;height:66px}
  .brand{position:absolute;left:0;top:0;display:flex;align-items:center;gap:12px}
  .brand-mark{width:64px;height:64px;border-radius:50%;background:var(--blue)}
  .brand-name{font-size:44px;font-weight:800;line-height:1;color:var(--ink);letter-spacing:-0.5px}
  .brand-tagline{font-size:12px;font-weight:700;color:var(--ink);margin-top:2px}
  .main-nav{position:absolute;right:0;top:28px;display:flex;gap:56px}
  .main-nav a{font-size:14px;font-weight:700;color:var(--ink);text-decoration:none;letter-spacing:.2px;padding-bottom:4px}
  .main-nav a.is-user{color:var(--blue);border-bottom:2px solid var(--blue)}
  .panel{position:absolute;background:var(--panel);border:1px solid var(--line)}
  .welcome{left:160px;top:110px;width:380px;height:90px;display:flex;align-items:center;padding-left:18px;gap:12px}
  .avatar{width:46px;height:46px;border-radius:50%;border:2px solid var(--line);background:#f0f0f0}
  .welcome strong{display:block;font-size:14px;font-weight:800}
  .welcome span{font-size:14px;color:var(--ink-soft)}
  .setup-btn{position:absolute;left:545px;top:110px;width:224px;height:89px;
    background:linear-gradient(180deg,var(--blue) 0%,var(--blue-light) 100%);
    border-bottom:4px solid var(--blue-dark);color:#fff;font-size:19px;font-weight:700;
    display:flex;align-items:center;justify-content:center;text-decoration:none}
  .servers{left:160px;top:205px;width:609px;height:277px;overflow:hidden}
  .col-tint{position:absolute;top:0;bottom:0;background:var(--panel-tint)}
  .servers table{position:relative;border-collapse:collapse;margin:18px 0 0 20px;width:570px;font-size:14px}
  .servers th{color:var(--blue);font-weight:700;text-align:left;height:38px;border-bottom:1px solid var(--line)}
  .servers td{height:32px;border-bottom:1px solid var(--line);color:var(--ink-soft)}
  .servers .c-status{text-align:center}
  .servers .c-chart{text-align:center}
  .servers td.c-level{color:var(--ink)}
  .ok{color:var(--ok);font-weight:700}
  .ok.faint{color:#e4f1e1}
  .summary{left:773px;top:110px;width:267px;height:372px}
  .summary-item{padding:18px 24px;height:80px;border-bottom:1px solid var(--line)}
  .summary-item.is-active{background:#fbfbfb}
  .summary-item h3{font-size:20px;font-weight:400;color:var(--ink)}
  .summary-item a{font-size:14px;color:var(--blue);text-decoration:none}
  .summary-item.is-idle h3{color:var(--muted)}
  .summary-item.is-idle p{font-size:14px;color:var(--muted)}
  .site-footer{position:absolute;left:160px;top:520px;width:880px;height:90px;display:flex;align-items:center}
  .footer-nav{display:flex;gap:18px}
  .footer-nav a{font-size:14px;color:var(--ink-soft);text-decoration:none}
  .copyright{font-size:14px;color:var(--ink-soft);margin-left:22px}
  .social{margin-left:auto;display:flex;gap:7px}
  .social span{width:24px;height:24px;background:var(--social);display:block}
  .social span.is-hot{background:var(--social-hot)}
</style>
</head>
<body>
  <div class="stage" role="img" aria-label="Light grey cracked concrete texture background"></div>

  <header class="site-header">
    <div class="brand">
      <div class="brand-mark"></div>
      <div>
        <div class="brand-name">Velkari</div>
        <div class="brand-tagline">Instant server setup &amp; In-depth monitoring</div>
      </div>
    </div>
    <nav class="main-nav">
      <a href="#">HOME</a><a href="#">SERVICES</a><a href="#">ABOUT US</a><a href="#">CONTACT</a><a href="#" class="is-user">HELLO! USER</a>
    </nav>
  </header>

  <section class="panel welcome">
    <div class="avatar"></div>
    <div><strong>Welcome!</strong><span>First Name</span></div>
  </section>

  <a class="setup-btn" href="#">Setup New Server</a>

  <section class="panel servers">
    <div class="col-tint" style="left:110px;width:206px"></div>
    <div class="col-tint" style="left:408px;width:50px"></div>
    <table>
      <thead><tr>
        <th style="width:106px">Server name</th>
        <th style="width:190px">Selected profile</th>
        <th class="c-status" style="width:100px">Status</th>
        <th class="c-chart" style="width:50px">
          <svg width="14" height="12" viewBox="0 0 14 12"><g fill="#1ba6dc"><rect x="0" y="5" width="2" height="7"/><rect x="3" y="2" width="2" height="10"/><rect x="6" y="4" width="2" height="8"/><rect x="9" y="1" width="2" height="11"/><rect x="12" y="3" width="2" height="9"/></g></svg>
        </th>
        <th style="padding-left:18px">Subscription Level</th>
      </tr></thead>
      <tbody>
        <tr><td>Server 1</td><td>Monitoring only</td><td class="c-status"><span class="ok">Ok</span></td>
          <td class="c-chart"><svg width="14" height="12" viewBox="0 0 14 12"><g fill="#aaa"><rect x="0" y="5" width="2" height="7"/><rect x="3" y="2" width="2" height="10"/><rect x="6" y="4" width="2" height="8"/><rect x="9" y="1" width="2" height="11"/><rect x="12" y="3" width="2" height="9"/></g></svg></td>
          <td class="c-level" style="padding-left:18px">Basic (?)</td></tr>
        <tr><td>Server 2</td><td>PHP FPM webserver</td><td class="c-status"><span class="ok">Ok</span></td>
          <td class="c-chart"><svg width="14" height="12" viewBox="0 0 14 12"><g fill="#aaa"><rect x="0" y="5" width="2" height="7"/><rect x="3" y="2" width="2" height="10"/><rect x="6" y="4" width="2" height="8"/><rect x="9" y="1" width="2" height="11"/><rect x="12" y="3" width="2" height="9"/></g></svg></td>
          <td class="c-level" style="padding-left:18px">Gold (?)</td></tr>
        <tr><td>Server 3</td><td>Select Profile...</td><td class="c-status"><span class="ok faint">Ok</span></td><td></td><td></td></tr>
      </tbody>
    </table>
  </section>

  <aside class="panel summary">
    <div class="summary-item is-active"><h3>You have:</h3><a href="#">5 Prepaid Setups Left</a></div>
    <div class="summary-item is-idle"><h3>You have:</h3><p>3 Subscriptions</p></div>
  </aside>

  <footer class="site-footer">
    <nav class="footer-nav"><a href="#">Home</a><a href="#">Services</a><a href="#">About Us</a><a href="#">Contact</a><a href="#">Sitemap</a></nav>
    <span class="copyright">© 2015 All Rights Reserved.</span>
    <div class="social"><span></span><span class="is-hot"></span><span></span></div>
  </footer>
</body>
</html>
```